Amazing Homepage required for Ireland's Top Crowdfunding site

Design/ PSD Files required.

BrightHarbour.com is the market leader in crowd lending/peer to peer lending in Ireland. Businesses/SME’s can borrow anything from €5,000 to €100,000 at interest rates much more favourable than those offered by the banks. BH is also a quicker and less bureaucratic than traditional lending institutions. We are a viable alternative to banks and traditional sources of finance.

Our lenders are members of the public and they can lend directly to Irish businesses in amounts from €50 to €2,000. They get a better rate of return than deposit accounts, as well as the feel good factor of supporting a local business.

We have just completed a full rebrand of our logo and colours and would now like to utilise these to best effect by implementing them in a total redesign of our homepage to attract borrowers and lenders. Please see the attached files for the brand guidelines and logo/colours to be used.

We are looking for a designer to utilise our new branding in a creative way, conveying that we are modern, trustworthy, competitive and friendly/local.

We currently have two different user groups:
1- Lenders; this currently consists of members of the public but in future will expand to include financial institutions

2- Business borrowers looking for funds for their business

Embracing and balancing both of these user groups is difficult so we would like the homepage to primarily target borrowers but incorporate clear alternative calls to action for lenders/prospective lenders as well.

We would like:
Infinite scroll homepage
New logo and tagline on a fixed header which should also include; ‘Marketplace’ ‘About’ ‘FAQ’ and a clear login button
A static full bleed image
Overlaid over this we would like a loan calculator in a similar style/functionality to this one on www.quellmoor.com. It should have:
an image of a slider icon with amounts from €0 to €100,000
A text field with ‘Business Loan amount’ which fills when the slider is moved
Then, a text field called ‘Monthly repayment’
An email field with a clear call to action ie ‘Go’ or ‘Get Started’
The purpose of this is to enable prospective borrowers to quickly and easily get a quote estimate for their loan
Underneath this we would like to have an alternate call to action to target prospective lenders; something like ‘Looking to Lend?’

Further down the page we would like to have a heading ‘What is Bright Harbour?’
(include information from company overview)

3 images to illustrate loans live in our Marketplace

Target Market(s)

This Homepge should appeal to small business owners

Industry/Entity Type

Crowd

Number of Pages Required

1 page

Font styles to use
Sans Serif

Requirements
Must have
• Linear clean and modern homepage
• Clear calls to action
Nice to have
• Ideas for how video/rich media might be incorporated into a future iteration of the homepage

```html
<!DOCTYPE html>
<html lang="en">
<head>
<meta charset="utf-8">
<title>Bright Harbour – Business Loans</title>
<link href="https://fonts.googleapis.com/css2?family=Open+Sans:wght@400;600;700;800&display=swap" rel="stylesheet">
<style>
:root{
  --accent:#e9472a;
  --accent-dark:#c93a20;
  --ink:#2b2b2b;
  --muted:#8a8a8a;
  --dark:#1f1f1f;
  --dark-2:#2b2b2b;
  --light:#f3f3f3;
  --line:#dcdcdc;
  --white:#ffffff;
}
*{box-sizing:border-box;margin:0;padding:0}
html,body{width:1200px;height:3429px;overflow:hidden}
body{font-family:"Open Sans",Arial,sans-serif;color:var(--ink);background:var(--white);position:relative}
section,header,footer{position:absolute;left:0;width:1200px;overflow:hidden}
.abs{position:absolute}
.hl{color:var(--accent)}

/* header */
.site-header{top:0;height:55px;background:var(--white);border-bottom:1px solid var(--line);z-index:5}
.brand{left:140px;top:8px;font-weight:700;font-size:24px;color:var(--ink);display:flex;align-items:center;gap:8px}
.brand .mark{width:24px;height:24px;border:2px solid var(--accent);border-radius:50%}
.brand small{position:absolute;left:32px;top:30px;font-size:9px;color:var(--accent);font-weight:600;white-space:nowrap}
.main-nav{left:740px;top:18px;display:flex;gap:46px;font-size:12px;color:#555}
.hdr-btn{position:absolute;top:16px;height:22px;width:52px;font-size:10px;font-weight:700;color:#fff;text-align:center;line-height:22px}
.hdr-btn.dark{left:1060px;background:#3a3a3a}
.hdr-btn.orange{left:1125px;background:var(--accent)}

/* hero */
.hero{top:55px;height:648px}
.hero-photo{left:0;top:0;width:1200px;height:648px;background:linear-gradient(100deg,#b8b2aa 0%,#d9d6d1 30%,#efedea 55%,#f7f6f4 100%)}
.hero-veil{left:0;top:0;width:1200px;height:648px;background:linear-gradient(90deg,rgba(255,255,255,0) 30%,rgba(255,255,255,.75) 55%,rgba(255,255,255,.35) 100%)}
.calc{left:144px;top:110px;width:324px;height:440px;background:rgba(255,255,255,.96);box-shadow:0 2px 10px rgba(0,0,0,.15);border-top:4px solid var(--accent)}
.calc h2{position:absolute;left:0;right:0;top:18px;text-align:center;font-size:30px;font-weight:800;color:#333}
.calc .sub{position:absolute;left:0;right:0;top:58px;text-align:center;font-size:10px;color:var(--muted)}
.calc .lbl{position:absolute;left:22px;font-size:9px;color:#666;text-transform:uppercase;font-weight:600}
.track{position:absolute;left:22px;width:282px;height:4px;background:#ddd}
.track i{position:absolute;left:0;top:0;height:4px;background:var(--accent)}
.track b{position:absolute;top:-6px;width:16px;height:16px;border-radius:50%;background:var(--accent);border:3px solid #fff;box-shadow:0 0 0 1px var(--accent)}
.range-ends{position:absolute;left:22px;width:282px;display:flex;justify-content:space-between;font-size:9px;color:#888}
.calc-field{position:absolute;left:22px;width:282px;height:32px;border:1px solid var(--line);background:#fff;display:flex;justify-content:space-between;align-items:center;padding:0 10px;font-size:10px;color:#777}
.calc-field strong{font-size:13px;color:#333}
.email-row{position:absolute;left:22px;top:346px;width:282px;height:40px;display:flex}
.email-row .email{flex:1;border:1px solid var(--line);border-right:0;font-size:10px;color:#aaa;line-height:38px;padding:0 10px;background:#fff}
.email-row .cta{width:112px;background:var(--accent);color:#fff;font-weight:700;font-size:13px;text-align:center;line-height:40px}
.lend-link{position:absolute;left:0;right:0;top:402px;text-align:center;font-size:11px;color:#555}
.lend-link b{color:var(--accent)}

.hero-copy{left:456px;top:150px;width:460px;text-align:center}
.hero-copy h1{font-size:30px;font-weight:800;color:var(--accent);letter-spacing:.5px}
.hero-copy h3{font-size:25px;font-weight:800;color:#333;line-height:1.1}
.hero-copy .note{font-size:11px;color:#555}
.hero-intro{left:640px;top:265px;width:300px;font-size:10px;color:#555;line-height:1.5}
.step{left:628px;width:320px;display:flex;gap:16px}
.step .num{flex:0 0 50px;height:50px;border-radius:50%;background:var(--accent);color:#fff;font-weight:700;font-size:22px;text-align:center;line-height:50px}
.step h4{font-size:18px;font-weight:700;color:#333}
.step p{font-size:10px;color:#666;line-height:1.4;width:190px}
.step-line{left:652px;width:2px;background:#bbb}

/* what is */
.whatis{top:703px;height:547px;background:#f4f4f4}
.section-title{position:absolute;left:0;width:1200px;text-align:center;font-size:24px;font-weight:800;letter-spacing:1px}
.section-sub{position:absolute;left:0;width:1200px;text-align:center;font-size:11px;color:#666}
.title-rule{position:absolute;left:570px;width:60px;height:3px;background:var(--accent)}
.whatis .body{left:150px;top:165px;width:900px;font-size:10.5px;line-height:1.75;color:#666;text-align:center}
.whatis .body p{margin-bottom:14px}

/* marketplace */
.market{top:1250px;height:585px;background:#fff}
.market-item{left:150px;width:380px;display:flex;gap:18px}
.market-item .ico{flex:0 0 54px;height:54px;border-radius:50%;background:#1e1e1e;position:relative}
.market-item .ico svg{position:absolute;left:13px;top:13px}
.market-item h4{font-size:13px;font-weight:700;color:var(--accent);margin-top:6px}
.market-item p{font-size:10px;line-height:1.5;color:#666;margin-top:4px;width:230px}
.market-photo{left:600px;top:210px;width:600px;height:375px;background:linear-gradient(135deg,#dfe4ea 0%,#c5ccd5 45%,#9aa3ae 100%)}

/* testimonials */
.trust{top:1835px;height:377px;background:var(--dark)}
.trust-box{left:149px;top:90px;width:163px;height:205px;border:2px solid var(--accent);padding:14px 12px;text-align:center;color:#ccc;font-size:9.5px;line-height:1.5}
.trust-box .btn{display:block;margin:12px auto 8px;width:110px;height:24px;background:var(--accent);color:#fff;font-weight:700;font-size:10px;line-height:24px}
.trust-box .ph-lbl{font-size:9px;color:#aaa}
.trust-box .ph{font-size:15px;font-weight:700;color:var(--accent)}
.trust h2{position:absolute;left:336px;top:58px;width:560px;font-size:23px;font-weight:800;color:#fff;text-align:center}
.trust h2 span{color:var(--accent)}
.video{top:115px;width:155px;height:125px;background:linear-gradient(135deg,#4a4a4a,#6d6a64);border:3px solid #fff}
.video .play{position:absolute;left:58px;top:42px;width:34px;height:34px;border-radius:50%;background:rgba(233,71,42,.9)}
.video .play:after{content:"";position:absolute;left:13px;top:9px;border-left:12px solid #fff;border-top:8px solid transparent;border-bottom:8px solid transparent}
.cap{top:252px;width:155px;text-align:center;font-size:10px;color:#fff;white-space:nowrap}
.cap em{font-style:normal;color:var(--accent)}
.arrow{top:160px;font-size:26px;color:#777}

/* form */
.apply{top:2212px;height:531px;background:#f1f1f1}
.field{height:26px;background:#fff;border:1px solid #e2e2e2;font-size:9px;color:#aaa;padding:0 10px;line-height:24px;position:absolute}
.field.sel:after{content:"";position:absolute;right:10px;top:10px;border-top:5px solid var(--accent);border-left:4px solid transparent;border-right:4px solid transparent}
.apply .submit{left:385px;top:362px;width:190px;height:28px;background:var(--accent);color:#fff;font-size:10px;font-weight:700;text-align:center;line-height:28px}
.apply .hours{left:600px;top:360px;font-size:9.5px;color:#666;line-height:1.4}

/* clients */
.clients{top:2743px;height:360px;background:#fff}
.client-row{left:180px;width:840px;display:flex;justify-content:center;gap:26px}
.client{display:flex;align-items:center;gap:6px;font-size:11px;font-weight:700;color:#9a9a9a;white-space:nowrap;height:30px}
.client i{flex:0 0 14px;height:14px;background:#c8c8c8}
.client.big{font-size:17px;font-weight:700;letter-spacing:.5px}

/* footer */
.site-footer{top:3103px;height:326px;background:var(--dark-2);color:#aaa}
.foot-nav{left:0;top:0;width:1200px;height:36px;display:flex;justify-content:center;gap:36px;font-size:10px;color:#ccc;line-height:36px;border-bottom:1px solid #3a3a3a}
.foot-nav .on{color:var(--accent)}
.foot-brand{left:190px;top:80px;font-size:26px;font-weight:700;color:#fff;display:flex;gap:8px;align-items:center}
.foot-brand .mark{width:26px;height:26px;border:2px solid var(--accent);border-radius:50%}
.foot-phone{left:450px;top:74px;font-size:9px}
.foot-phone strong{display:block;font-size:22px;color:var(--accent);font-weight:700}
.foot-req{left:690px;top:82px;width:170px;height:30px;border:1px solid #888;color:#fff;font-size:10px;font-weight:700;line-height:28px;text-align:center}
.foot-col{top:150px;width:210px;font-size:9.5px;line-height:1.55}
.foot-col h5{color:#fff;font-size:13px;margin-bottom:6px}
.foot-col a{display:block;color:var(--accent);text-decoration:none}
.foot-map{left:830px;top:150px;width:180px;height:110px;background:linear-gradient(135deg,#e8e4da,#d3d8cf)}
.social{display:flex;gap:6px;margin-top:8px}
.social i{width:14px;height:14px;border-radius:50%;border:1px solid var(--accent)}
</style>
</head>
<body>

<header class="site-header">
  <div class="brand abs"><span class="mark"></span>Bright Harbour<small>the business lending people</small></div>
  <nav class="main-nav abs"><span>The Marketplace</span><span>About us</span><span>FAQ</span></nav>
  <div class="hdr-btn dark">Join</div>
  <div class="hdr-btn orange">Login</div>
</header>

<section class="hero">
  <div class="hero-photo abs" role="img" aria-label="Photo of a person working at a laptop on a wooden desk"></div>
  <div class="hero-veil abs"></div>

  <div class="calc abs">
    <h2>HOW <span class="hl">MUCH</span></h2>
    <p class="sub">Get your business loan quote in a minute</p>
    <span class="lbl" style="top:92px">How much would your business like to borrow?</span>
    <div class="track" style="top:124px"><i style="width:70px"></i><b style="left:62px"></b></div>
    <div class="range-ends" style="top:140px"><span>€0</span><span>€100,000</span></div>
    <span class="lbl" style="top:172px">Business loan amount</span>
    <div class="calc-field" style="top:188px"><span>€</span><strong>25,000</strong></div>
    <span class="lbl" style="top:234px">Monthly repayment</span>
    <div class="calc-field" style="top:250px"><span>36 months</span><strong>€812</strong></div>
    <span class="lbl" style="top:310px">Your email address</span>
    <div class="email-row"><span class="email">name@business.ie</span><span class="cta">GET STARTED</span></div>
    <p class="lend-link">Looking to lend? <b>Start lending from €50 ›</b></p>
  </div>

  <div class="hero-copy abs">
    <h1>BUSINESS FINANCE</h1>
    <h3>Borrow up to €100,000</h3>
    <p class="note">funded by local lenders, faster than the banks</p>
  </div>
  <p class="hero-intro abs">Getting started takes only a few minutes. Complete a short form online and we will review your request and reply quickly.</p>

  <div class="step-line abs" style="top:340px;height:200px"></div>
  <div class="step abs" style="top:315px"><span class="num">1</span><div><h4>GET A QUOTE</h4><p>Tell us how much you need and see your quote right away.</p></div></div>
  <div class="step abs" style="top:415px"><span class="num">2</span><div><h4>SIGN A CONTRACT</h4><p>Review the simple terms and sign online in minutes.</p></div></div>
  <div class="step abs" style="top:515px"><span class="num">3</span><div><h4>RECEIVE MONEY</h4><p>Funds arrive in your business account within days.</p></div></div>
</section>

<section class="whatis">
  <h2 class="section-title" style="top:58px">WHAT IS <span class="hl">BRIGHT HARBOUR</span></h2>
  <p class="section-sub" style="top:95px">Business lending made simple, local and fair</p>
  <div class="title-rule" style="top:118px"></div>
  <div class="body abs">
    <p>Bright Harbour is a peer to peer lending marketplace that connects Irish businesses with members of the public who want to lend. Businesses can borrow anything from €5,000 to €100,000 at rates that compare well with the banks, and the process is faster and less bureaucratic than traditional lending. Lenders choose the businesses they back, starting from just €50, and watch their money help a local company grow while earning a better return than a deposit account. <span class="hl">Every loan is reviewed by our credit team</span> before it reaches the marketplace, so lenders can see clear information about each business.</p>
    <p>We started with one simple idea: good Irish businesses deserve access to fair finance, and people deserve a better home for their savings. Since then thousands of lenders have funded companies in every county, from cafés and workshops to tech start-ups and family farms. Our team is based in Ireland and we are always happy to talk through your plans by phone or in person.</p>
    <p>Applying is easy. Tell us about your business and how much you need, and we will give you a quote estimate in minutes. Once approved, your loan is listed in the marketplace and typically funded within days. Repayments are fixed and monthly, with no hidden fees and no penalty for paying early.</p>
  </div>
</section>

<section class="market">
  <h2 class="section-title" style="top:90px">OUR <span class="hl">MARKET PLACE</span></h2>
  <p class="section-sub" style="top:128px">We are ready to offer you several types of loans</p>
  <div class="title-rule" style="top:150px"></div>

  <div class="market-item abs" style="top:230px">
    <span class="ico"><svg width="28" height="28" viewBox="0 0 28 28"><circle cx="14" cy="14" r="12" fill="none" stroke="#fff" stroke-width="2"/><text x="14" y="19" text-anchor="middle" fill="#fff" font-size="14" font-weight="700" font-family="Open Sans,sans-serif">$</text></svg></span>
    <div><h4>CONSUMER CREDIT</h4><p>Flexible personal credit for everyday needs, with clear monthly repayments and fair rates.</p></div>
  </div>
  <div class="market-item abs" style="top:340px">
    <span class="ico"><svg width="28" height="28" viewBox="0 0 28 28"><circle cx="14" cy="14" r="12" fill="none" stroke="#fff" stroke-width="2"/><text x="14" y="18" text-anchor="middle" fill="#fff" font-size="10" font-weight="700" font-family="Open Sans,sans-serif">24</text></svg></span>
    <div><h4>URGENT LOAN</h4><p>Fast decisions for urgent business needs, with funds released within one working day.</p></div>
  </div>
  <div class="market-item abs" style="top:450px">
    <span class="ico"><svg width="28" height="28" viewBox="0 0 28 28"><circle cx="14" cy="14" r="12" fill="none" stroke="#fff" stroke-width="2"/><text x="14" y="19" text-anchor="middle" fill="#fff" font-size="14" font-weight="700" font-family="Open Sans,sans-serif">$</text></svg></span>
    <div><h4>SAMPLE LOAN</h4><p>A simple starter loan for small firms taking their first step with marketplace lending.</p></div>
  </div>

  <div class="market-photo abs" role="img" aria-label="Photo of a smiling business team giving thumbs up in an office"></div>
</section>

<section class="trust">
  <div class="trust-box abs">
    <p>We can get you funded within <span class="hl">a few days</span> of your application. Getting started is easy and our friendly team is here to help you at every step.</p>
    <span class="btn">APPLY NOW</span>
    <p class="ph-lbl">Call us</p>
    <p class="ph">086-555-0142</p>
  </div>
  <h2>TRUSTED BY <span>100+</span> IRISH BUSINESS OWNERS</h2>
  <span class="arrow abs" style="left:340px">‹</span>
  <div class="video abs" style="left:370px" role="img" aria-label="Video still of a customer testimonial"><span class="play"></span></div>
  <div class="video abs" style="left:540px" role="img" aria-label="Video still of a customer testimonial"><span class="play"></span></div>
  <span class="arrow abs" style="left:710px">›</span>
  <p class="cap abs" style="left:370px">Oliver from Greenvale, <em>Dublin</em></p>
  <p class="cap abs" style="left:540px">Olivier from Stonebridge, <em>Dublin</em></p>
</section>

<section class="apply">
  <h2 class="section-title" style="top:68px">APPLY <span class="hl">FORM</span></h2>
  <p class="section-sub" style="top:102px">Fill the form below and we will contact you shortly</p>
  <div class="title-rule" style="top:122px"></div>

  <div class="field" style="left:150px;top:172px;width:210px">First name</div>
  <div class="field" style="left:375px;top:172px;width:210px">Last name</div>
  <div class="field" style="left:600px;top:172px;width:210px">Email address</div>
  <div class="field sel" style="left:825px;top:172px;width:225px;color:#555">Managed</div>

  <div class="field" style="left:150px;top:212px;width:210px">Phone number</div>
  <div class="field" style="left:375px;top:212px;width:210px">Company name</div>
  <div class="field" style="left:600px;top:212px;width:210px">Loan amount</div>
  <div class="field" style="left:825px;top:212px;width:225px">Loan term</div>

  <div class="field" style="left:150px;top:252px;width:210px">Business type</div>
  <div class="field" style="left:375px;top:252px;width:210px">Years trading</div>

  <div class="field" style="left:150px;top:292px;width:900px;height:50px">Tell us about your business</div>

  <div class="submit abs">LEAVE LOAN REQUEST</div>
  <p class="hours abs">Loan 24/7 Now!<br>Office hours Mon – Fri 9am to 6pm</p>
</section>

<section class="clients">
  <h2 class="section-title" style="top:55px">OUR <span class="hl">CLIENT</span></h2>
  <div class="title-rule" style="top:92px"></div>
  <div class="client-row abs" style="top:118px">
    <div class="client"><i></i>Northgate Enterprise</div>
    <div class="client"><i></i>Harbourline Enterprise</div>
    <div class="client"><i></i>Ashford Chamber</div>
    <div class="client"><i></i>Riverton Chamber</div>
  </div>
  <div class="client-row abs" style="top:168px">
    <div class="client"><i></i>Smallfirm Alliance</div>
    <div class="client"><i></i>Merrow Traders</div>
    <div class="client"><i></i>Calder Direct</div>
    <div class="client"><i></i>Brennock &amp; Co</div>
  </div>
  <div class="client-row abs" style="top:218px">
    <div class="client"><i></i>Wavetalk</div>
    <div class="client"><i></i>Venture Plus</div>
  </div>
  <div class="client-row abs" style="top:266px;gap:60px">
    <div class="client big">The Coastal Ledger</div>
    <div class="client big">Western Courier</div>
  </div>
</section>

<footer class="site-footer">
  <nav class="foot-nav abs"><span class="on">Home</span><span>The Marketplace</span><span>About us</span><span>FAQ</span><span>Venture Source</span><span>Blog</span><span>Contact us</span></nav>
  <div class="foot-brand abs"><span class="mark"></span>Bright Harbour</div>
  <div class="foot-phone abs">Ireland<strong>204.5550.100200</strong></div>
  <div class="foot-req abs">REQUEST A LOAN NOW</div>

  <div class="foot-col abs" style="left:190px"><h5>About</h5><p>Bright Harbour is a lending marketplace helping Irish businesses grow with fair, fast finance funded by local people.</p></div>
  <div class="foot-col abs" style="left:430px"><h5>Loan Areas</h5><a>Consumer credit</a><a>Urgent loan</a><a>Sample loan</a><a>Business loan</a><a>Lend with us</a></div>
  <div class="foot-col abs" style="left:620px"><h5>Ireland</h5><p>12 Quay Street, Dublin 2<br>Mon – Fri 9am to 6pm<br><span class="hl">hello@brightharbour.com</span></p><div class="social"><i></i><i></i><i></i><i></i></div></div>
  <div class="foot-map abs" role="img" aria-label="Street map showing the office location"></div>
</footer>

</body>
</html>
```